TALVEXO needs a Sleek, Professional and Serious Web Design, this web design is aiming to be famous!

Dear Designers,

We need a web design for a new company based on the Internet named "talvexo". I have already worked with PQ to get my logo and it has been a wonderful experience which I want to repeat. We are kind of work social network, the web page will be mostly used to write comments on businesses around the world to help workers find which company fit the best for them. This website is also here to help people finding work by giving them the tools to make the right research.

For contents inspiration, you could see on the added files a sketch of the website but I am not asking you following it because it was just for giving the contents.

We do not have any example regarding website that we do like because all are coming so generic. We would like a very sleek website, where surfing become very intuitive and ergonomic (Glimmerly is not very ergonomic for example from our point of view). The website must reflect professionalism and seriousness and worker, world connexion.

We will be pleased to accept original designs as long as they fit to our requirements and if it is properly made of course: e.g. web page looking like a newspaper etc.

About colours, we are not decided yet but we are aiming a light orange (pastel style) or dark bluish green. Also, it comes to our attention that a web site mostly realized in grey-scale will be very interesting (touch of colour will be accepted as well if it miss too much dynamism) .

We will give the feedback as soon as possible because we would like to have 5 pages but it will be only very small changes on the next ones. (like adding 4 buttons)

Target Market(s)

Our target is relatively large because it is all people of working age, in numbers we can say a range of people aged from 18 to 45 years.

Industry/Entity Type

Internet

Number of Pages Required

3 page

Font styles to use
Sans Serif

Requirements
Must have
• Elements that must be on the web page are exposed below:
• - company logo ( .ai & .eps files on added files)
• - 4 buttons (Searcher "highlighted" / Advises / Jobs / Solutions)
• - login/account window
• - language button (e.g. a flag)
• - Window companies searcher (the most important, refer to the sketch)
• - classic menu down the page - about us / contact us / conditions / site map / community / politics / publicity / languages / copyright etc.
Nice to have
• We want a professional and serious website.
Should not have
• If you have a doubt, just ask us because nothing are coming to our mind.

```html
<!DOCTYPE html>
<html lang="en">
<head>
<meta charset="utf-8">
<title>TALVEXO – Home</title>
<link rel="stylesheet" href="https://fonts.googleapis.com/css2?family=Oswald:wght@300;400&family=Open+Sans:wght@400;600&display=swap">
<style>
:root{
  --orange:#f7963a;
  --hero-dark:#5e5e5e;
  --hero-mid:#8a8a8a;
  --hero-light:#b9b9b9;
  --bar:#4b4b4b;
  --white:#ffffff;
  --title:#666666;
  --muted:#c9c9c9;
  --rule:#e3e3e3;
  --footer:#3b3b3b;
  --footer-text:#a9a9a9;
}
*{margin:0;padding:0;box-sizing:border-box}
html,body{width:1200px;height:982px;overflow:hidden}
body{position:relative;background:var(--white);font-family:"Open Sans",sans-serif}
.hero{position:absolute;left:0;top:0;width:1200px;height:607px;
  background:linear-gradient(180deg,var(--hero-mid) 0%,var(--hero-light) 35%,var(--hero-mid) 62%,var(--hero-dark) 100%)}
.brand{position:absolute;left:101px;top:38px;display:flex;align-items:center;gap:8px;
  font-family:"Oswald",sans-serif;font-weight:400;font-size:40px;color:var(--white);letter-spacing:1px;line-height:44px}
.brand-dot{width:30px;height:30px;border-radius:50%;background:var(--white)}
.lang{position:absolute;left:889px;top:0;width:58px;height:34px;border:1px solid #c8c8c8;border-top:0;
  background:rgba(255,255,255,.15);font-family:"Oswald",sans-serif;font-size:13px;color:#555;
  display:flex;align-items:center;justify-content:center;gap:5px}
.lang-flag{width:14px;height:9px;background:linear-gradient(180deg,#3c4a8c 0 45%,#d44 45% 60%,#fff 60% 75%,#d44 75%)}
.account{position:absolute;left:957px;top:0;width:133px;height:33px;background:var(--bar);
  font-family:"Oswald",sans-serif;font-size:17px;color:var(--white);display:flex;align-items:center;justify-content:center;gap:12px}
.nav{list-style:none;font-family:"Oswald",sans-serif;font-weight:300;font-size:15px;color:var(--white)}
.nav li{position:absolute;top:50px;height:31px;line-height:31px;white-space:nowrap}
.nav li.active{background:var(--bar);width:66px;text-align:center}
.hero-title{position:absolute;left:0;top:186px;width:1200px;text-align:center;
  font-family:"Oswald",sans-serif;font-weight:400;font-size:45px;line-height:51px;color:#f2f2f2}
.hero-sub{position:absolute;left:0;top:304px;width:1200px;text-align:center;font-size:21px;color:#f4f4f4}
.search{position:absolute;left:111px;top:369px;width:979px;height:84px;border:1px solid #e0e0e0;background:rgba(255,255,255,.06)}
.field{position:absolute;top:20px;height:40px;background:var(--white);border:1px solid #ddd;
  font-size:13px;color:#555;padding-left:10px;line-height:38px}
.search-btn{position:absolute;left:801px;top:20px;width:146px;height:40px;background:var(--orange);
  font-family:"Oswald",sans-serif;font-size:22px;color:var(--white);text-align:center;line-height:40px}
.features{position:absolute;left:0;top:607px;width:1200px;height:321px;
  background:linear-gradient(180deg,#f3f3f3 0%,#ffffff 55%)}
.divider{position:absolute;top:0;width:1px;height:321px;background:var(--rule)}
.feature{position:absolute;top:0;width:300px;height:321px;text-align:center}
.feature-icon{position:absolute;top:55px;left:108px;width:84px;height:84px}
.feature-title{position:absolute;top:153px;left:0;width:100%;font-family:"Oswald",sans-serif;font-weight:400;font-size:20px;color:var(--title)}
.feature-text{position:absolute;top:190px;left:0;width:100%;font-size:13.5px;line-height:20px;color:var(--muted);font-weight:600;white-space:nowrap}
.footer{position:absolute;left:0;top:928px;width:1200px;height:54px;background:var(--footer);
  font-size:13px;color:var(--footer-text)}
.footer-links{position:absolute;left:112px;top:18px;display:flex;gap:10px;list-style:none;white-space:nowrap}
.copyright{position:absolute;right:334px;top:17px;font-size:13px;white-space:nowrap}
.social{position:absolute;right:110px;top:19px;display:flex;gap:8px;list-style:none;font-size:9.5px;color:var(--orange);white-space:nowrap}
</style>
</head>
<body>
<header class="hero" role="img" aria-label="Greyscale city skyline seen from a footbridge with railings">
  <div class="brand"><span class="brand-dot"></span>TALVEXO</div>
  <div class="lang"><span class="lang-flag"></span>EN</div>
  <div class="account"><span>Login</span><span>|</span><span>Signup</span></div>
  <ul class="nav">
    <li class="active" style="left:437px">HOME</li>
    <li style="left:540px">COMPANY</li>
    <li style="left:648px">ADVISES</li>
    <li style="left:744px">JOBS</li>
    <li style="left:819px">SOLUTIONS</li>
    <li style="left:928px">ABOUT US</li>
    <li style="left:1021px">CONTACT US</li>
  </ul>
  <h1 class="hero-title">Welcome To TALVEXO<br>Providing Better Solution for your Problems</h1>
  <p class="hero-sub">Search Over 2 Million People, Advises Jobs &amp; Solutions</p>
  <div class="search">
    <div class="field" style="left:23px;width:206px">Company Name VAT Number</div>
    <div class="field" style="left:242px;width:156px">City</div>
    <div class="field" style="left:410px;width:176px">Post Code</div>
    <div class="field" style="left:598px;width:186px">Country</div>
    <div class="search-btn">SEARCH NOW</div>
  </div>
</header>

<section class="features">
  <span class="divider" style="left:425px"></span>
  <span class="divider" style="left:774px"></span>
  <div class="feature" style="left:112px">
    <svg class="feature-icon" viewBox="0 0 84 84"><circle cx="42" cy="42" r="40" fill="none" stroke="#f7963a" stroke-width="3"/>
      <rect x="24" y="36" width="26" height="18" rx="3" fill="#f7963a"/><path d="M30 54 L28 60 L36 54Z" fill="#f7963a"/>
      <rect x="44" y="24" width="18" height="12" rx="3" fill="none" stroke="#f7963a" stroke-width="2"/></svg>
    <h2 class="feature-title">TALVEXO ADVISES</h2>
    <p class="feature-text">Lorem ipsum dolor sit amet, consecte-<br>tur adipiscing elit, sed do eiusmod<br>tempor incididunt ut labore et dolore<br>magna aliqua.</p>
  </div>
  <div class="feature" style="left:450px">
    <svg class="feature-icon" viewBox="0 0 84 84"><circle cx="42" cy="42" r="42" fill="#d3d3d3"/>
      <rect x="28" y="26" width="28" height="34" rx="2" fill="#fff"/>
      <rect x="32" y="32" width="20" height="3" fill="#d3d3d3"/><rect x="32" y="39" width="20" height="2" fill="#d3d3d3"/>
      <rect x="32" y="45" width="20" height="2" fill="#d3d3d3"/><rect x="32" y="51" width="14" height="2" fill="#d3d3d3"/></svg>
    <h2 class="feature-title">TALVEXO JOBS</h2>
    <p class="feature-text">Lorem ipsum dolor sit amet, consecte-<br>tur adipiscing elit, sed do eiusmod<br>tempor incididunt ut labore et dolore<br>magna aliqua.</p>
  </div>
  <div class="feature" style="left:787px">
    <svg class="feature-icon" viewBox="0 0 84 84"><circle cx="42" cy="42" r="40" fill="none" stroke="#f7963a" stroke-width="3"/>
      <circle cx="42" cy="40" r="10" fill="#f7963a"/><rect x="37" y="49" width="10" height="9" rx="2" fill="#f7963a"/>
      <g stroke="#f7963a" stroke-width="2"><line x1="42" y1="22" x2="42" y2="26"/><line x1="26" y1="40" x2="30" y2="40"/><line x1="54" y1="40" x2="58" y2="40"/><line x1="31" y1="29" x2="34" y2="32"/><line x1="53" y1="29" x2="50" y2="32"/></g></svg>
    <h2 class="feature-title">TALVEXO SOLUTIONS</h2>
    <p class="feature-text">Lorem ipsum dolor sit amet, consecte-<br>tur adipiscing elit, sed do eiusmod<br>tempor incididunt ut labore et dolore<br>magna aliqua.</p>
  </div>
</section>

<footer class="footer">
  <ul class="footer-links"><li>About us</li><li>Contact us</li><li>Conditions</li><li>Site map</li><li>Community</li></ul>
  <p class="copyright">© Copyright Talvexo.com.All Right Reserved.</p>
  <ul class="social"><li>Glimmerly</li><li>Chirpo</li><li>Linkra</li><li>Plusa</li><li>Pinvo</li><li>Feed</li></ul>
</footer>
</body>
</html>
```